Herbal Apothecary Rebrand

I am in the process of merging two companies Wren Hollow Oils and Among The Pines Apothecary. I am dissolving Wren Hollow Oils (WHO) and need to blend a few of the products into the Among The Pines Apothecary (ATP) line. These blended products will take on a fresh new look. This is where I need some help. I have a few ideas but need some creative genius to bring them together.
The following products need to be merged and once a logo is agreed upon I will be working with this designer with further pay to create the following:
~ body oils (labels and packaging) **existing product shown in image A-1
~ plant bath medicines (labels and packaging) **a new product with the bottle and packaging shown in images attached
~ facial serum (labels and packaging - the packaging will be the same cardboard boxes used for the body oils) **existing product shown in
image A-2
~ teas (labeling) **a new product - packaging sample pics attached
~ as well as having the ability to carry over into the creation of 40 different essential oil containers. ** An idea I have is shown in image C-1.
Ideas...
I prefer distinct lines, square designs vs circular or curvy. I prefer clean and clear vs busy.
I like the layout shown in images A-1 & A-2 and could see moving forward with a very similar style without the indigenous logo. I would like to see what it looks like to have the ATP logo (building with trees) in place of the indigenous logo. ** I am open to reworking the ATP logo to make it a bit more vertical in size vs being quite small and horizontal. This could include revising or recreating the building and trees altogether.
I like the speckled background (shown in image B-1), it gives the sense that it is aged and goes with the Apothecary theme, however I'm not completely attached to it.
I like the off white labels that I currently have for the BODY OILS and the SERUM and I am leaning towards this as the colour for the new blended line. I would also be open to seeing a lighter version of the turquoise.
This is just an idea that I have however I am open to something completely new. What is important is that it blends nicely with the current line of products available at ATP (the entire line can be seen online). There is a good chance that I will be merging the products over to the new and improved design as we move through the older packaging.
Notes on Plant Bath labels:
**If working from the current layout of the Body Oil labels this can be used as an example to create a template
~ The top will have the new or reworked logo (with or without the company name depending on space available)
~ First line for each bottle will have a name eg: NETTLE + ROSE
~ Second line will be the purpose of the medicine eg: HEART OPENING
~ The next line will read: PLANT BATH
~Then space for a little blurb eg: BRINGING BALANCE TO THE EMOTIONAL AND ENERGETIC HEALTH OF THE HEART.
~ The size of the bottle will read 400 ML but in a vertical direction on the bottle
Notes on Tea labels:
The teas have not been created yet but I'm looking for some ideas that follow in the same design as the Plant Bath labels so the following can be used as an example:
~ Name; TULSI + ROSE
~ The purpose: ELEVATED HEART
~ The bottom will read: LOOSE TEA
~ Blurb about the benefits: A TRANSFORMATIONAL CREATION OF WARM NOTES WITH DEEP WOODY UNDERTONES. THIS ANYTIME TEA IS AS PLEASING IN THE HEALTH BENEFITS AS IT IS TO THE TASTE.
~ Include the size: 100g
**I maxed out in pictures so I wasn't able to add more inspiration pics but I also quite like the moss & kettle tea line (shows up in a google search) as its clean and clear. The difference being I won't be printing directly on the packaging, it will need to be a label.
Logo Text
I would like to see if we can incorporate the name AMONG THE PINES APOTHECARY however this might make it too busy. Perhaps smaller lettering for "among the pines" and larger for "APOTHECARY". It also might be the case that adding this on the front makes things look too busy. I'm open to creative suggestions.

```html
<!DOCTYPE html>
<html lang="en">
<head>
<meta charset="utf-8">
<title>Among The Pines Apothecary – Cardamom + Cypress Warming Body Oil Label</title>
<link href="https://fonts.googleapis.com/css2?family=Advent+Pro:wght@300;400;500;600&display=swap" rel="stylesheet">
<style>
  :root {
    --surround: #dcdcdc;
    --paper: #f5f4f1;
    --ink: #2a1a14;
    --ink-soft: #4a3a33;
    --art-light: #cfcdc9;
    --art-dark: #5b5753;
  }
  * { margin: 0; padding: 0; box-sizing: border-box; }
  html, body {
    width: 1200px; height: 889px; overflow: hidden;
    background: var(--surround);
  }
  .label {
    position: absolute; left: 33px; top: 27px; width: 1134px; height: 828px;
    background: var(--paper);
    font-family: "Advent Pro", "Arial Narrow", sans-serif;
    color: var(--ink);
  }
  .brand {
    position: absolute; left: 0; top: 40px; width: 100%;
    text-align: center; font-weight: 500; font-size: 30px;
    letter-spacing: 3px; line-height: 38px; color: var(--ink);
  }
  .brand .brand-main { font-size: 40px; line-height: 46px; letter-spacing: 4px; }
  .crest {
    position: absolute; left: 309px; top: 156px; width: 531px; height: 228px;
  }
  .product { position: absolute; left: 327px; width: 484px; line-height: 1; white-space: nowrap; }
  .rule { position: absolute; left: 327px; height: 2px; background: var(--ink); }
  .product-name { top: 417px; font-size: 44px; font-weight: 500; letter-spacing: 1px; }
  .product-type { top: 490px; font-size: 44px; font-weight: 500; letter-spacing: 1px; }
  .product-claim { top: 572px; font-size: 36px; font-weight: 300; letter-spacing: 1px; color: var(--ink-soft); }
  .product-blurb {
    top: 634px; width: 360px; font-size: 28px; font-weight: 300;
    letter-spacing: 2px; line-height: 36px; color: var(--ink-soft);
  }
  .divider { position: absolute; left: 701px; top: 638px; width: 2px; height: 103px; background: var(--ink); }
  .volume {
    position: absolute; left: 733px; top: 736px;
    transform-origin: top left; transform: rotate(-90deg);
    font-size: 42px; font-weight: 600; letter-spacing: 2px; line-height: 40px; white-space: nowrap;
  }
  .info-panel {
    position: absolute; left: 918px; top: 71px; width: 165px; height: 689px;
    border: 2px solid var(--ink);
  }
  .web {
    position: absolute; left: 1052px; top: 546px;
    transform-origin: top left; transform: rotate(-90deg);
    font-size: 18px; font-weight: 400; letter-spacing: 2px; white-space: nowrap; color: var(--ink-soft);
  }
  .side-copy {
    position: absolute; left: 40px; top: 807px; width: 700px;
    transform-origin: top left; transform: rotate(-90deg);
    font-size: 17px; font-weight: 400; letter-spacing: 3.2px; line-height: 25px;
    color: var(--ink-soft); white-space: nowrap;
  }
  .side-copy .ingredients { margin-top: 18px; letter-spacing: 3px; }
</style>
</head>
<body>
  <main class="label">
    <div class="brand">among the pines<br><span class="brand-main">APOTHECARY</span></div>

    <svg class="crest" viewBox="0 0 531 228" role="img" aria-label="Illustration of a small wooden cabin with a porch and rocking chairs, flanked by two windswept trees on a grassy patch">
      <defs>
        <radialGradient id="crestTone" cx="50%" cy="55%" r="60%">
          <stop offset="0%" stop-color="#5b5753"/>
          <stop offset="100%" stop-color="#cfcdc9" stop-opacity="0.5"/>
        </radialGradient>
      </defs>
      <rect width="531" height="228" fill="url(#crestTone)"/>
    </svg>

    <div class="product product-name">CARDAMOM + CYPRESS</div>
    <div class="rule" style="top:479px;width:484px"></div>
    <div class="product product-type">WARMING BODY OIL</div>
    <div class="rule" style="top:550px;width:484px"></div>
    <div class="product product-claim">ORGANIC BOTANICALS</div>
    <div class="rule" style="top:621px;width:484px"></div>
    <div class="product product-blurb">REVITALIZING AND<br>STIMULATING FOR A<br>RENEWED SENSE OF SPIRIT</div>
    <div class="divider"></div>
    <div class="volume">1ØØML</div>
    <div class="rule" style="top:759px;width:480px"></div>

    <div class="info-panel"></div>
    <div class="web">WWW.WRENHOLLOWOILS.COM</div>

    <div class="side-copy">
      <p>SUGGESTED USE:</p>
      <p>WARM OIL IF DESIRED. APPLY TO THE FULL BODY AFTER BATHING, MASSAGE</p>
      <p>IN MOTIONS TOWARD THE HEART UNTIL THE OIL IS MOSTLY ABSORBED. CAN</p>
      <p>ALSO BE ADDED TO BATH WATER.</p>
      <p class="ingredients">*SUNFLOWER OIL, **ORANGE, **CARDAMOM, **CYPRESS, **GINGER *ORGANIC.</p>
    </div>
  </main>
</body>
</html>
```